Luxury Eco accommodation needs new website

Luxury lodge accommodation on exclusive private property in Flinders Ranges South Australia.
Brand new venture needs new site.
Focus on small group accommodation on exclusive property with outdoor experiences. Mountain biking , bush walking, outdoor dining.
We currently have a website but are having trouble making it our own. Needs to be "polished" by a professional.
Can you help?

www.tallowridgehomestead.com.au

Target Market(s)

High income travellers, luxury accommodation

Industry/Entity Type

Accommodation

```html
<!DOCTYPE html>
<html lang="en">
<head>
<meta charset="utf-8">
<title>Tallow Ridge Homestead – Luxury Lodge</title>
<link rel="stylesheet" href="https://fonts.googleapis.com/css2?family=Carlito:wght@400;700&family=Uncial+Antiqua&display=swap">
<style>
  :root {
    --bg: #1f1f1f;
    --bg-dark: #181818;
    --text: #e4e0da;
    --text-dim: #cfcac3;
    --heading: #f1ebe2;
    --accent: #f2c9bd;
    --nav-box: #2c2b2a;
    --nav-active: #3a2624;
    --dash: #4a4a4a;
    --caption: rgba(78, 66, 52, 0.88);
    --logo-bg: #ffffff;
    --logo-ink: #2a3040;
  }
  * { box-sizing: border-box; margin: 0; padding: 0; }
  html, body { width: 1200px; height: 929px; overflow: hidden; }
  body {
    position: relative;
    background:
      repeating-linear-gradient(45deg, rgba(255,255,255,0.015) 0 2px, transparent 2px 4px),
      radial-gradient(ellipse at 50% 40%, #262626 0%, var(--bg) 55%, var(--bg-dark) 100%);
    font-family: "Carlito", "Calibri", sans-serif;
    color: var(--text);
  }
  .logo {
    position: absolute; left: 195px; top: 9px; width: 170px; height: 141px;
    background: var(--logo-bg);
    display: flex; flex-direction: column; justify-content: center; align-items: center;
    color: var(--logo-ink); font-size: 22px; letter-spacing: 2px; line-height: 1.2; text-align: center;
  }
  .main-nav { position: absolute; top: 110px; left: 587px; height: 23px; }
  .main-nav a {
    position: absolute; top: 0; height: 23px; line-height: 23px;
    font-size: 14px; color: var(--text); text-decoration: none; text-align: center;
    background: var(--nav-box); border-radius: 2px;
  }
  .main-nav a.is-active { background: var(--nav-active); color: var(--accent); }
  .rule {
    position: absolute; left: 0; width: 1200px; height: 0;
    border-top: 2px dashed var(--dash);
  }
  .slide { position: absolute; box-shadow: 0 10px 18px rgba(0,0,0,0.7); }
  .slide--side-left { left: 215px; top: 193px; width: 132px; height: 248px;
    background: linear-gradient(90deg, #c9ccc8 0%, #8c8a80 45%, #3d3932 100%); }
  .slide--side-right { left: 854px; top: 191px; width: 134px; height: 245px;
    background: linear-gradient(90deg, #2a2522 0%, #8a5a32 40%, #c47a3a 60%, #5b4a3a 100%); }
  .slide--main { left: 347px; top: 179px; width: 507px; height: 294px; overflow: hidden;
    background: linear-gradient(180deg, #7ba0cc 0%, #c8d4e2 35%, #b5b6b2 55%, #8a8260 75%, #6a5e44 100%); }
  .slide-zoom { position: absolute; left: 231px; top: 118px; }
  .slide-caption {
    position: absolute; left: 0; bottom: 0; width: 100%; height: 79px;
    background: var(--caption); padding: 14px 19px 0;
    font-size: 11px; line-height: 17px; color: #f4efe8;
  }
  .slide-reflection { position: absolute; left: 347px; top: 473px; width: 507px; height: 42px;
    background: linear-gradient(180deg, rgba(90,80,64,0.35), rgba(30,30,30,0)); }
  .info-block { position: absolute; top: 548px; }
  .info-block h2 {
    font-family: "Uncial Antiqua", serif; font-weight: 400; font-size: 28px;
    color: var(--heading); margin-bottom: 14px; letter-spacing: 0.5px;
  }
  .info-block p { font-size: 12.5px; line-height: 20.6px; color: var(--text-dim); }
  .info--about { left: 189px; width: 270px; }
  .info--testimonial { left: 502px; width: 275px; }
  .info--contact { left: 808px; width: 240px; }
  .info--contact h2 { margin-bottom: 12px; }
  .contact-line { display: flex; align-items: center; gap: 14px; font-size: 12.5px; height: 21px; color: var(--text-dim); }
  .contact-line svg { width: 25px; flex: none; }
</style>
</head>
<body>
  <header>
    <div class="logo"><span>TALLOW RIDGE</span><span>HOMESTEAD</span></div>
    <nav class="main-nav">
      <a class="is-active" href="#" style="left:0;width:92px">LUXURY LODGE</a>
      <a href="#" style="left:110px;width:92px">ABOUT US</a>
      <a href="#" style="left:219px;width:93px">GALLERY</a>
      <a href="#" style="left:329px;width:94px">CONTACT</a>
    </nav>
  </header>
  <div class="rule" style="top:152px"></div>

  <section class="slider">
    <div class="slide slide--side-left" role="img" aria-label="Photo of a guest on the lodge deck overlooking the ranges"></div>
    <div class="slide slide--side-right" role="img" aria-label="Photo of the lodge's timber and corrugated iron wall at sunset"></div>
    <div class="slide-reflection"></div>
    <div class="slide slide--main" role="img" aria-label="Photo of the lodge buildings on a grassy ridge under a blue sky">
      <svg class="slide-zoom" width="42" height="42" viewBox="0 0 42 42">
        <circle cx="21" cy="21" r="19" fill="none" stroke="#b8383a" stroke-width="2"/>
        <path d="M21 11v20M11 21h20" stroke="#b8383a" stroke-width="4"/>
      </svg>
      <p class="slide-caption">Wattle Cottage is a fully restored miner's cottage constructed of native pine and local stone. The cottage offers a cosy and comfortable environment from which to enjoy visiting the Blinman district.</p>
    </div>
  </section>

  <section class="info-block info--about">
    <h2>About us</h2>
    <p>Tallow Ridge Lodge is nestled in the heart of SA's magnificent Flinders Ranges. It is located on Tallow Ridge Homestead, 480 kms north of Adelaide and stretches along the northern boundary of the great Flinders Ranges National Park. The Lodge is tucked into a ridge top near the homestead and overlooks a valley of river red gums and native pines.</p>
  </section>

  <section class="info-block info--testimonial">
    <h2>Testimonial</h2>
    <p>Recently upgraded quality Shearer's Quarters style accommodation, ideal for groups and families and sleeping up to 18 people. Fully self-contained, with large kitchen plus dining/living area; wood fire and gas heating; 240 volt solar power; large outdoor deck and BBQ area, nestled alongside river red gum-lined homestead creek.</p>
  </section>

  <section class="info-block info--contact">
    <h2>Contact</h2>
    <p>For bookings &amp; information:<br>Fundacja Przykładowa<br>Kraków, ul. Lipowa 7, woj. małopolskie</p>
    <div class="contact-line">
      <svg viewBox="0 0 25 18" height="18"><path d="M2 6c0-4 21-4 21 0v2h-5V6c-3-1-8-1-11 0v2H2z M7 8h11l3 9H4z" fill="#e4e0da"/><circle cx="12.5" cy="12.5" r="2.5" fill="#1f1f1f"/></svg>
      <span>(08) 8600 1234</span>
    </div>
    <div class="contact-line">
      <svg viewBox="0 0 25 16" height="16"><rect x="0" y="0" width="25" height="16" fill="#e4e0da"/><path d="M0 0l12.5 9L25 0" fill="none" stroke="#1f1f1f" stroke-width="1.5"/></svg>
      <span>stay@tallowridgehomestead.com.au</span>
    </div>
  </section>

  <div class="rule" style="top:806px"></div>
</body>
</html>
```